Zeb-Ka.com Eliquid Bottling and insert flyer

Bottle:

We need a new bottle design; I have included the design but we are not hung up on the overall design.. We do not want it kid friendly tho! No cartoon graphics and things along those lines.

These must fit on an korvel standard 30 up label (2-5/8 x 1)
We want our name logo and brand name on the front. Along with a "space" where we can thermally print the e-juice name

Must have the following verbage on it

Contains
Nicotine, USP Propylene Glycol, USP Vegetable Glycerin, Artificial Food Grade Flavorings
Not for sale to minors
Made in the USA (Little USA Flag logo)
Shake well before use.
Keep out of reach
of children & Pets.

We would like options in small circles for nicotine levels, 24, 18, 9, 6,0 mg that we can use a small marker to highlight.

The juice brand is called "Glim'r Juice"
Born on date is optional
The name needs to be in a area so we can custom print them via thermal printer

Insert:
We also need an insert announcing our company and a "XX" off coupon code We want a small spot where we can print the code along with the percentage
This will need to be in a standard format, 3x5 must have the domain name www.zeb-ka.com and use the attached logos, everything else is full creativity

```html
<!DOCTYPE html>
<html lang="en">
<head>
<meta charset="utf-8">
<title>Glim'r Juice bottle label</title>
<link rel="stylesheet" href="https://fonts.googleapis.com/css2?family=Source+Sans+3:wght@400;600;700&family=Roboto+Condensed:wght@700&display=swap">
<style>
  :root {
    --brand-purple: #6b419a;
    --label-white: #ffffff;
    --backdrop-light: #f4f4f4;
    --backdrop-dark: #d9d9d9;
    --ink-dark: #111111;
    --sign-red: #d7261e;
    --flag-red: #c8313a;
    --flag-blue: #3a4f9a;
  }
  * { box-sizing: border-box; margin: 0; padding: 0; }
  html, body { width: 1200px; height: 806px; overflow: hidden; }
  body {
    position: relative;
    background: radial-gradient(ellipse at center, var(--backdrop-light) 0%, var(--backdrop-dark) 100%);
    font-family: "Source Sans 3", sans-serif;
  }
  .label {
    position: absolute; left: 50px; top: 200px; width: 1100px; height: 404px;
    background: var(--label-white);
    box-shadow: 0 2px 6px rgba(0,0,0,.12);
  }
  .band { position: absolute; left: 0; width: 100%; background: var(--brand-purple); color: var(--label-white); }
  .band-top { top: 0; height: 62px; }
  .band-bottom { bottom: 0; height: 60px; }
  .domain { position: absolute; left: 68px; top: 10px; font-size: 34px; font-weight: 600; letter-spacing: .5px; }
  .juice-name { position: absolute; left: 515px; top: 8px; font-size: 42px; font-weight: 600; letter-spacing: 6px; }
  .born-on { position: absolute; left: 117px; top: 5px; font-size: 21px; font-weight: 600; line-height: 26px; }
  .contents { position: absolute; left: 330px; width: 758px; top: 9px; text-align: center;
    font-family: "Roboto Condensed", sans-serif; font-weight: 700; font-size: 15.5px; line-height: 22px; }
  .checklist { position: absolute; left: 58px; top: 92px; list-style: none; color: var(--brand-purple); font-size: 22px; line-height: 26px; }
  .checklist li { position: relative; padding-left: 30px; margin-bottom: 11px; }
  .checklist li::before { content: "✔"; position: absolute; left: 0; top: 0; font-size: 19px; }
  .wordmark { position: absolute; display: flex; align-items: center; color: var(--brand-purple); font-weight: 600; }
  .wordmark-main { left: 430px; top: 82px; font-size: 118px; letter-spacing: -2px; gap: 28px; }
  .wordmark-small { left: 64px; top: 262px; font-size: 45px; gap: 12px; }
  .wordmark .dot { border-radius: 50%; background: var(--brand-purple); }
  .wordmark-main .dot { width: 96px; height: 96px; }
  .wordmark-small .dot { width: 36px; height: 36px; }
  .origin { position: absolute; left: 376px; top: 249px; width: 120px; text-align: center; }
  .flag { width: 118px; height: 66px; background: linear-gradient(180deg, var(--flag-red) 0%, #e88a8e 50%, var(--flag-red) 100%); position: relative; }
  .flag::before { content: ""; position: absolute; left: 0; top: 0; width: 50px; height: 36px; background: var(--flag-blue); }
  .origin-text { font-family: "Roboto Condensed", sans-serif; font-weight: 700; font-size: 17px; color: var(--ink-dark); margin-top: 4px; }
  .nicotine { position: absolute; left: 598px; top: 243px; width: 224px; text-align: center; color: var(--brand-purple); }
  .nicotine h2 { font-size: 22px; font-weight: 700; letter-spacing: .5px; line-height: 26px; }
  .levels { display: flex; margin-top: 4px; border: 3px solid var(--brand-purple); border-radius: 9px; height: 54px; }
  .levels span { flex: 1; display: flex; align-items: center; justify-content: center; font-size: 21px; color: var(--ink-dark); }
  .levels span + span { border-left: 2px solid var(--brand-purple); }
  .age-sign { position: absolute; left: 937px; top: 247px; }
</style>
</head>
<body>
  <section class="label">
    <header class="band band-top">
      <div class="domain">ZEB-KA.COM</div>
      <div class="juice-name">GLIM'R JUICE</div>
    </header>

    <ul class="checklist">
      <li>Shake well before use</li>
      <li>Not for sale to minors</li>
      <li>Keep out of reach<br>of children &amp; Pets</li>
    </ul>

    <div class="wordmark wordmark-main"><span>Zeb-Ka</span><span class="dot"></span></div>
    <div class="wordmark wordmark-small"><span>Zeb-Ka</span><span class="dot"></span></div>

    <div class="origin">
      <div class="flag" role="img" aria-label="Small United States flag"></div>
      <div class="origin-text">Made in USA</div>
    </div>

    <div class="nicotine">
      <h2>NICOTINE LEVELS</h2>
      <div class="levels"><span>24</span><span>18</span><span>9</span><span>6</span><span>0</span></div>
    </div>

    <svg class="age-sign" width="90" height="90" viewBox="0 0 90 90" aria-label="Not for under 18">
      <circle cx="45" cy="45" r="40" fill="#fff" stroke="var(--sign-red)" stroke-width="5"/>
      <text x="45" y="30" text-anchor="middle" font-family="Roboto Condensed, sans-serif" font-weight="700" font-size="8" fill="#111">UNDER</text>
      <text x="45" y="66" text-anchor="middle" font-family="Roboto Condensed, sans-serif" font-weight="700" font-size="40" fill="#111">18</text>
      <line x1="17" y1="17" x2="73" y2="73" stroke="var(--sign-red)" stroke-width="5"/>
    </svg>

    <footer class="band band-bottom">
      <div class="born-on">Born on date<br>mm/dd/yy</div>
      <div class="contents">Contains<br>Nicotine, USP Propylene Glycol, USP Vegetable Glycerin, Artificial Food Grade Flavorings</div>
    </footer>
  </section>
</body>
</html>
```